Business Card Design needed for logo design project

Would like a professional business card for a company involved in financial and latest technologies including CAD design. We would like the card to convey professionalism and communicate that we are involved in up to date technology solutions.

Target Market(s)

Business 2 Business sales

Industry/Entity Type

Financial

Colors

Designer to choose colors to be used in the design.

Requirements
Must have
• Business Name
Logo
Name
Phone
Email
Nice to have
• Website

```html
<!DOCTYPE html>
<html lang="en">
<head>
<meta charset="utf-8">
<title>Vantrex Business Card</title>
<link href="https://fonts.googleapis.com/css2?family=Saira:wght@400;500;600&display=swap" rel="stylesheet">
<style>
  :root {
    --backdrop: #2b2b2d;
    --card-white: #f7f7f7;
    --brand-red: #d41f27;
    --brand-navy: #0f1a45;
    --ghost-grey: #e4e6ea;
    --text-white: #ffffff;
  }
  * { margin: 0; padding: 0; box-sizing: border-box; }
  html, body {
    width: 1200px; height: 798px; overflow: hidden;
    background: var(--backdrop);
    font-family: "Saira", sans-serif;
  }
  .business-card {
    position: absolute; left: 110px; top: 119px;
    width: 980px; height: 560px;
    background: var(--card-white);
    overflow: hidden;
    box-shadow: 0 10px 30px rgba(0,0,0,.45);
  }
  .header-band {
    position: absolute; left: 0; top: 0; width: 100%; height: 160px;
    background: var(--brand-red);
  }
  .company-name {
    position: absolute; left: 50px; top: 38px;
    font-size: 78px; font-weight: 600; letter-spacing: 4px;
    color: var(--text-white); line-height: 1;
  }
  .header-contact {
    position: absolute; right: 44px; top: 62px;
    text-align: right; color: var(--text-white);
    font-size: 30px; font-weight: 500; line-height: 1.2; letter-spacing: 1px;
  }
  .background-motif {
    position: absolute; left: 20px; top: 200px; width: 940px; height: 230px;
  }
  .person {
    position: absolute; left: 230px; top: 205px;
  }
  .person-name {
    font-size: 118px; font-weight: 500; color: var(--brand-navy); line-height: 1;
  }
  .person-title {
    margin-top: 4px; margin-left: 4px;
    font-size: 44px; font-weight: 500; color: var(--brand-red); line-height: 1;
  }
  .accent-line {
    position: absolute; left: 0; top: 430px; width: 100%; height: 12px;
    background: var(--brand-red);
  }
  .footer-band {
    position: absolute; left: 0; top: 442px; width: 100%; height: 118px;
    background: var(--brand-navy); color: var(--text-white);
  }
  .footer-mobile {
    position: absolute; left: 50px; top: 14px; font-size: 36px; font-weight: 500;
  }
  .footer-email {
    position: absolute; right: 44px; bottom: 8px; font-size: 38px; font-weight: 500;
  }
  .footer-label { font-size: 24px; font-weight: 400; }
</style>
</head>
<body>
  <div class="business-card">
    <div class="header-band">
      <div class="company-name">VANTREX</div>
      <div class="header-contact">
        <div class="header-phone">00 5550 1234</div>
        <div class="header-web">www.vantrex.com</div>
      </div>
    </div>

    <svg class="background-motif" viewBox="0 0 940 230" role="img" aria-label="Faint wireframe drawing of the company lettering">
      <defs>
        <linearGradient id="motifFade" x1="0" y1="0" x2="1" y2="1">
          <stop offset="0" stop-color="#eceef1"/>
          <stop offset="1" stop-color="#dfe2e7"/>
        </linearGradient>
      </defs>
      <rect x="0" y="0" width="940" height="230" fill="url(#motifFade)" opacity="0.6"/>
    </svg>

    <div class="person">
      <div class="person-name">Your Name</div>
      <div class="person-title">Managing Director</div>
    </div>

    <div class="accent-line"></div>
    <div class="footer-band">
      <div class="footer-mobile"><span class="footer-label">mobile: </span>0400 555 019</div>
      <div class="footer-email"><span class="footer-label">email: </span>info@vantrex.com</div>
    </div>
  </div>
</body>
</html>
```